SofaVoyager ClipHarbor page redesign needed

SofaVoyager specializes in static, long play, ambient, experiential videos that allow viewers to vicariously enjoy the sights and sounds of fascinating locations around the world. The channel lets you enjoy the sights and sounds of beaches, markets, European cafes, fountains, skylines, train stations, etc. The SofaVoyager library consists of over 3,000 travel videos from around the world that are broadcast n television and shown on OrchardView and Zenta, but we need to improve our ClipHarbor presence-- and we need your help. Can you help us design a new ClipHarbor channel @sofavoyager that borrows the best features from other 4K travel video channels? We want to begin offering dozens of 8-hour videos with different background sounds for viewers: natural sound, brown noise, piano classical music and jazz. Can you help us become one of the top ambient channels on ClipHarbor?

Visit here to learn more:
http://sofavoyager.example
https://www.instagram.com/sofavoyager/
https://www.facebook.com/sofavoyager

Keywords: travel, ambient, 4K, cafe, study, brown noise, white noise, relaxing, work and study, jazz, focus, chill, piano, nature, slow television
Updates

Hoping to get some more creative designs.

Here are 2,100 videos that will be on the ClipHarbor channel. Please use still images from these actual videos for the ClipHarbor page. https://vimeo.com/sofavoyager

```html
<!DOCTYPE html>
<html lang="en">
<head>
<meta charset="utf-8">
<title>SofaVoyager channel banner</title>
<link rel="stylesheet" href="https://fonts.googleapis.com/css2?family=Bebas+Neue&family=Poppins:wght@600;700&display=swap">
<style>
  :root {
    --canvas: #d4d5d8;
    --band: #000000;
    --panel-a: #1b1b1b;
    --panel-b: #0c0c0c;
    --ink: #ffffff;
    --ink-dark: #111111;
  }
  * { margin: 0; padding: 0; box-sizing: border-box; }
  html, body { width: 1200px; height: 1200px; overflow: hidden; }
  body {
    background: var(--canvas);
    position: relative;
  }
  .channel-banner {
    position: absolute;
    left: 40px;
    top: 504px;
    width: 1120px;
    height: 192px;
    background: var(--band);
    box-shadow: 0 10px 24px rgba(0,0,0,.25);
    overflow: hidden;
  }
  .safe-panel {
    position: absolute;
    left: 199px;
    top: 0;
    width: 741px;
    height: 192px;
    background: linear-gradient(135deg, var(--panel-a), var(--panel-b) 55%, var(--panel-a));
  }
  .gallery {
    position: absolute;
    left: 0; top: 0;
    width: 1120px; height: 192px;
  }
  .brand {
    position: absolute;
    left: 207px;
    top: 44px;
    width: 140px;
    color: var(--ink);
  }
  .brand-top {
    font-family: "Poppins", sans-serif;
    font-weight: 700;
    font-size: 24px;
    line-height: 26px;
    letter-spacing: -0.3px;
  }
  .brand-main {
    font-family: "Bebas Neue", sans-serif;
    font-size: 54px;
    line-height: 48px;
    letter-spacing: 0.2px;
    margin-top: 2px;
  }
  .brand-url {
    display: inline-block;
    margin-top: 6px;
    background: var(--ink);
    color: var(--ink-dark);
    font-family: "Bebas Neue", sans-serif;
    font-size: 12.5px;
    line-height: 19px;
    padding: 0 5px;
    letter-spacing: 0.2px;
  }
  .library-count {
    position: absolute;
    left: 800px;
    top: 42px;
    width: 136px;
    color: var(--ink);
    text-align: left;
  }
  .count-number {
    font-family: "Bebas Neue", sans-serif;
    font-size: 88px;
    line-height: 76px;
    letter-spacing: 1px;
  }
  .count-sub {
    font-family: "Poppins", sans-serif;
    font-weight: 600;
    font-size: 11px;
    line-height: 14px;
    margin-top: 2px;
  }
  .count-line {
    font-family: "Bebas Neue", sans-serif;
    font-size: 22px;
    line-height: 20px;
    letter-spacing: 0.3px;
  }
  .seal-name {
    font-family: "Poppins", sans-serif;
    font-weight: 700;
    font-size: 8.5px;
    fill: var(--ink);
  }
</style>
</head>
<body>
  <section class="channel-banner" aria-label="SofaVoyager channel banner">
    <div class="safe-panel"></div>

    <svg class="gallery" viewBox="0 0 1120 192" xmlns="http://www.w3.org/2000/svg">
      <defs>
        <linearGradient id="beach" x1="0" y1="0" x2="0" y2="1">
          <stop offset="0" stop-color="#1f4fb8"/>
          <stop offset="0.55" stop-color="#5f9be0"/>
          <stop offset="1" stop-color="#e9eef2"/>
        </linearGradient>
        <linearGradient id="falls" x1="0" y1="0" x2="0" y2="1">
          <stop offset="0" stop-color="#6d7a5e"/>
          <stop offset="0.5" stop-color="#4f6b33"/>
          <stop offset="1" stop-color="#6b5a36"/>
        </linearGradient>
        <linearGradient id="city" x1="0" y1="0" x2="0" y2="1">
          <stop offset="0" stop-color="#a9cbe8"/>
          <stop offset="0.5" stop-color="#6f8e6a"/>
          <stop offset="1" stop-color="#5d7a58"/>
        </linearGradient>
        <linearGradient id="harbour" x1="0" y1="0" x2="0" y2="1">
          <stop offset="0" stop-color="#9aa7b8"/>
          <stop offset="0.45" stop-color="#3f4a44"/>
          <stop offset="1" stop-color="#6f7f95"/>
        </linearGradient>
      </defs>

      <polygon role="img" aria-label="Photo: hammock between palm trees on a white sand beach"
               points="345,20 440,20 483,175 385,175" fill="url(#beach)" stroke="#fff" stroke-width="3"/>
      <polygon role="img" aria-label="Photo: waterfall over mossy rocks in a green garden"
               points="450,20 544,20 584,175 492,175" fill="url(#falls)" stroke="#fff" stroke-width="3"/>
      <polygon role="img" aria-label="Photo: city waterfront with a domed parliament building"
               points="598,20 690,20 647,175 581,175" fill="url(#city)" stroke="#fff" stroke-width="3"/>
      <polygon role="img" aria-label="Photo: marina with boathouses below forested mountains"
               points="694,20 792,20 748,175 656,175" fill="url(#harbour)" stroke="#fff" stroke-width="3"/>

      <g class="brand-seal">
        <circle cx="572" cy="98" r="37" fill="#fff"/>
        <circle cx="572" cy="98" r="32" fill="#151515"/>
        <text class="seal-name" x="572" y="101" text-anchor="middle">SofaVoyager</text>
      </g>
    </svg>

    <div class="brand">
      <div class="brand-top">SOFA</div>
      <div class="brand-main">VOYAGER</div>
      <div class="brand-url">WWW.SOFAVOYAGER.EXAMPLE</div>
    </div>

    <div class="library-count">
      <div class="count-number">3000</div>
      <div class="count-sub">TRAVEL VIDEOS FROM</div>
      <div class="count-line">AROUND THE WORLD</div>
    </div>
  </section>
</body>
</html>
```